〇依頼の目的/概要
電子書籍(readvo)の表紙デザインをおねがいします。

〇画像サイズ
表紙サイズの理想的な寸法は2560×1600ピクセルです。
注:画像の寸法は1000×625ピクセル以上であることが必要です。
画像の最大の寸法は10000×10000ピクセルです。

〇タイトル
花粉症は運動だけでは消えません!

〇帯キャッチ

・眠ることも許されない
死にたくなるようなかゆみと痛みから
柔らかい潤いのある肌になった

・人生の波と家族とのご縁をひもといて
薬を使わずに治す

・「絶対に治る、治ったら
同じように苦しんでいる人の為に役立つ本を書こう」
・・・と決めていました。

デザイナーさんの判断で、
どれかを使ってもらっても、
または全部を使ってもらってもOKです。

〇著者 ぽにゃりんカフェ 占導師 千景(沢井千景)

文字の大きさと配置と色のインパクトがあって一目惚れしました。
修正依頼にも迅速な対応もありがたかったです。

初めての電子書籍の執筆と初めてのジョブリオへの仕事依頼で、
ドキドキで、いろいろ小さなわからないところだらけでした。
たくさんの提案、どれも素敵なものばかりですべての提案者の方々に
感謝の氣持ちでいっぱいです。ありがとうございました。
これからもアトピー性皮膚炎を克服するための電子書籍を執筆していく予定なので
また、協力していただけたら嬉しいです。

```html
<!DOCTYPE html>
<html lang="ja">
<head>
<meta charset="utf-8">
<title>花粉症は運動だけでは消えません!</title>
<link rel="stylesheet" href="https://fonts.googleapis.com/css2?family=Noto+Sans+JP:wght@900&family=Noto+Serif+JP:wght@700;900&display=swap">
<style>
  :root {
    --ink: #1f1a17;
    --paper: #ffffff;
    --lime: #dcee00;
  }
  html, body { margin: 0; padding: 0; overflow: hidden; background: var(--paper); }
  .cover {
    position: relative; width: 760px; height: 1200px; overflow: hidden;
    background: var(--paper); color: var(--ink);
    font-family: "Noto Serif JP", serif; font-weight: 900;
  }
  .author {
    position: absolute; left: 30px; top: 26px;
    font-family: "Noto Sans JP", sans-serif; font-weight: 900; line-height: 1.3;
  }
  .author__cafe { font-size: 17px; }
  .author__title { font-size: 25px; }
  .author__name { font-size: 17px; margin-left: -4px; }

  .vertical { position: absolute; writing-mode: vertical-rl; line-height: 1; white-space: nowrap; }
  .title-subject { left: 600px; top: 16px; font-size: 68px; letter-spacing: -2px; }
  .title-key { left: 330px; top: 120px; font-size: 210px; letter-spacing: 10px; }
  .title-only { left: 220px; top: 150px; font-size: 42px; letter-spacing: -1px; }

  .exclaim { position: absolute; left: 0; top: 0; }
  .title-verb { left: 86px; top: 172px; font-size: 84px; letter-spacing: -2px; }

  .band {
    position: absolute; left: 0; top: 716px; width: 760px; height: 484px;
    background: var(--lime);
  }
  .band__lead { position: absolute; left: 34px; top: 22px; line-height: 1.45; }
  .band__quote { position: absolute; left: 34px; top: 272px; line-height: 1.4; }
  .txt-s { font-size: 22px; font-weight: 700; display: block; }
  .txt-l { font-size: 42px; display: block; line-height: 1.25; }
  .txt-xs { font-size: 16px; font-weight: 700; display: block; }
  .txt-m { font-size: 36px; }
  .txt-inline { font-size: 21px; font-weight: 700; }

  .promise { top: 20px; font-size: 60px; letter-spacing: -3px; }
  .promise--1 { left: 656px; }
  .promise--2 { left: 588px; }
  .promise--3 { left: 516px; }
  .promise--4 { left: 448px; }
  .promise--5 { left: 386px; }
</style>
</head>
<body>
<main class="cover">
  <div class="author">
    <div class="author__cafe">ぽにゃりんカフェ</div>
    <div class="author__title">占導師　千景</div>
    <div class="author__name">（沢井千景）</div>
  </div>

  <h1 class="title">
    <span class="vertical title-subject">花粉症は</span>
    <span class="vertical title-key">運動</span>
    <span class="vertical title-only">だけでは</span>
  </h1>

  <svg class="exclaim" width="760" height="740" viewBox="0 0 760 740" aria-hidden="true">
    <path d="M92 172 Q142 150 192 172 L160 602 L128 602 Z" fill="var(--lime)"/>
    <circle cx="146" cy="664" r="57" fill="var(--lime)"/>
  </svg>
  <span class="vertical title-verb">消えません</span>

  <section class="band">
    <p class="band__lead" style="margin:0">
      <span class="txt-s">眠ることも許されない</span>
      <span class="txt-s">死にたくなるような</span>
      <span class="txt-s">かゆみと痛みから</span>
      <span class="txt-l">柔らかい</span>
      <span class="txt-l">潤いのある肌</span>
      <span class="txt-xs">になった</span>
    </p>
    <p class="band__quote" style="margin:0">
      <span style="display:block"><span class="txt-inline">「絶対に治る、</span><span class="txt-m">治ったら</span></span>
      <span class="txt-s" style="font-size:21px">同じように苦しんでいる人の為に</span>
      <span class="txt-l" style="font-size:40px">役立つ本を書こう」</span>
      <span class="txt-s" style="font-size:19px">・・・と決めていました。</span>
    </p>
    <span class="vertical promise promise--1">人生の波と</span>
    <span class="vertical promise promise--2">家族とのご縁を</span>
    <span class="vertical promise promise--3">ひもといて</span>
    <span class="vertical promise promise--4">薬を使わずに</span>
    <span class="vertical promise promise--5">治す</span>
  </section>
</main>
</body>
</html>
```